Real Estate Company
Tolin Estate Partners
Project: Real Estate Company
Real Estate Company - Real Estate
Creative Brief
Professional
Dale Moxon
Broker
PO Box 3152 Fresno, CA 93729
dale@tolinestatepartners.com
www.tolinestatepartners.com
BRE # 04527391
Card should have rounded edges.
one side of card should have all the info and one side should have logo + website

```html
<!DOCTYPE html>
<html lang="en">
<head>
<meta charset="utf-8">
<title>Tolin Estate Partners – Business Card</title>
<link href="https://fonts.googleapis.com/css2?family=Lato:wght@300;400;700&display=swap" rel="stylesheet">
<style>
  :root {
    --page: #e9eaec;
    --card: #ffffff;
    --card-back: #c9ccd0;
    --blue: #1a86cf;
    --blue-deep: #0c63a8;
    --ink: #2d2f33;
    --ink-soft: #55585e;
    --on-blue: #ffffff;
  }
  * { margin: 0; padding: 0; box-sizing: border-box; }
  html, body {
    width: 1200px; height: 1086px; overflow: hidden;
    background: var(--page);
    font-family: "Lato", Arial, sans-serif;
  }
  .business-card {
    position: absolute; left: 180px;
    width: 840px; height: 480px;
    border-radius: 22px;
    overflow: hidden;
    box-shadow: 0 16px 36px rgba(0,0,0,0.18);
  }
  .card-front { top: 40px; background: var(--card); }
  .card-back {
    top: 566px; background: var(--card-back);
    display: flex; flex-direction: column; align-items: center; justify-content: center; gap: 26px;
  }
  .card-wave { position: absolute; inset: 0; }

  .brand { display: flex; align-items: center; gap: 18px; }
  .card-front .brand { position: absolute; left: 60px; top: 58px; }
  .brand-square { width: 52px; height: 52px; background: var(--blue); }
  .brand-name {
    font-size: 28px; font-weight: 400; letter-spacing: 4px;
    text-transform: uppercase; color: var(--blue-deep);
  }
  .back-website { font-size: 20px; font-weight: 300; color: var(--ink); letter-spacing: 1px; }

  .holder { position: absolute; right: 60px; top: 132px; text-align: right; }
  .holder-name {
    font-size: 28px; font-weight: 400; letter-spacing: 2px;
    text-transform: uppercase; color: var(--ink);
  }
  .holder-title { margin-top: 4px; font-size: 20px; font-weight: 300; color: var(--ink-soft); }
  .holder-licence { margin-top: 4px; font-size: 16px; font-weight: 300; color: var(--ink-soft); }

  .contact-group {
    position: absolute; top: 368px;
    color: var(--on-blue); font-size: 18px; font-weight: 300; line-height: 1.6;
  }
  .contact-phone { left: 60px; }
  .contact-address { left: 300px; }
  .contact-online { left: 540px; }
</style>
</head>
<body>
  <article class="business-card card-front">
    <svg class="card-wave" viewBox="0 0 840 480" width="840" height="480" aria-hidden="true">
      <defs>
        <linearGradient id="blueBand" x1="0" y1="0" x2="1" y2="1">
          <stop offset="0" stop-color="#2a98dd"/>
          <stop offset="1" stop-color="#0c63a8"/>
        </linearGradient>
      </defs>
      <path d="M0,270 C80,245 140,245 200,270 S320,300 400,270 S520,240 600,262 S760,295 840,262 V480 H0 Z" fill="url(#blueBand)"/>
      <g transform="translate(78,332)" fill="none" stroke="#fff" stroke-width="2.2">
        <circle r="17"/>
        <path d="M-6,-8 q-3,3 0,8 q3,7 10,9 q4,1 5,-2 l-3,-3 l-3,2 q-4,-3 -6,-7 l2,-3 z" fill="#fff" stroke="none"/>
      </g>
      <g transform="translate(318,332)" fill="none" stroke="#fff" stroke-width="2.2">
        <circle r="17"/>
        <path d="M0,10 L-6,-1 A7,7 0 1 1 6,-1 Z" fill="#fff" stroke="none"/>
        <circle cy="-3" r="2.5" fill="#1a86cf" stroke="none"/>
      </g>
      <g transform="translate(558,332)" fill="none" stroke="#fff" stroke-width="1.8">
        <circle r="17" stroke-width="2.2"/>
        <circle r="9"/>
        <ellipse rx="4" ry="9"/>
        <line x1="-9" y1="0" x2="9" y2="0"/>
      </g>
    </svg>

    <div class="brand">
      <span class="brand-square"></span>
      <span class="brand-name">Tolin Estate Partners</span>
    </div>

    <div class="holder">
      <p class="holder-name">Dale Moxon</p>
      <p class="holder-title">Broker</p>
      <p class="holder-licence">BRE # 04527391</p>
    </div>

    <div class="contact-group contact-phone">
      <p>559 204 3187</p>
      <p>559 204 3188</p>
    </div>
    <div class="contact-group contact-address">
      <p>PO Box 3152</p>
      <p>Fresno, CA 93729</p>
    </div>
    <div class="contact-group contact-online">
      <p>dale@tolinestatepartners.com</p>
      <p>www.tolinestatepartners.com</p>
    </div>
  </article>

  <article class="business-card card-back">
    <div class="brand">
      <span class="brand-square"></span>
      <span class="brand-name">Tolin Estate Partners</span>
    </div>
    <p class="back-website">www.tolinestatepartners.com</p>
  </article>
</body>
</html>
```